依頼詳細
現在、iDeCo、nISAセミナー・住宅ローンセミナーを両面や片面ずつの配布しています。今回よりQRコードで毎月のイベントから選べる方式に変更したいなと思います。その分、各セミナーの特徴を簡潔にしたいのと現在同業者との差別化になっている高い専門知識をもつFPが講師・参加費あり・相談料があり無理な勧誘が一切なしという当店舗の特徴を活かしたチラシにしたいです。
また県内ではほぼ100%(把握する限り)のこの類のセミナーはケーキ付無料セミナーなど集客に特化したものが多いです。
今回は差別化を意識したものを望みます。
記載項目
現在にチラシテンプレートをいくつか掲載します
サイズ
A6
ページ数
片面
希望イメージ
シンプル 複雑
単色 カラフル
暗い 明るい
日常 高級
遊び心 厳粛
未来的 伝統的
女性的 男性的
希望する色
緑系、青系、水色系
納品ファイル
• イラストレーター形式 (.ai)
補足説明
現在使用しているチラシデータと各セミナーのソラミネ用のURLを添付します。
①ローンセミナー
https://soramine.jp/landing_pages/view/qtr2m?_gl=1*k4p7zx*_gcl_au*QWx3NTk2MjE4OC4xNjk4ODg3NzIx&_ga=2.52914837.417208361.1701234567-398271640.1655512903

②iDeCoNISAセミナー
https://soramine.jp/landing_pages/view/58hwf?_gl=1*3r6t02b*_gcl_au*QWx3NTk2MjE4OC4xNjk4ODg3NzIx&_ga=2.64927318.417208361.1701234567-398271640.1655512903

当店の案内もURLより参考にしていただき、イメージをもって作成いただけると幸いです。
https://xwrtb.hp.soramine.jp/?_gl=1*720kq4n*_gcl_au*QWx3NTk2MjE4OC4xNjk4ODg3NzIx&_ga=2.158302746.417208361.1701234567-398271640.1655512903
よろしくお願いいたします。
2024年1月8日追記になります。
イメージとしては当店の仕組みや紹介をメイン。(認知・周知UP)
真ん中やみやすい位置に人気セミナーみたいな形でQRコードか何かで誘導してその先にLPがある形で考えています!またこの形にこだわりがあるわけではないので別案あればお願いします。最近周辺で同じ類のイベントが多いので差別化を考えています
1月14日
当店舗は毎月15万部ほどチラシをポスティングしています。
チラシのどこかに〇月イベントやセミナーといったような何月分のチラシなのか記載をしていただくとありがたいです。途中での依頼ですみませんがよろしくお願いします。
有料という部分が他とは大きく違います。ここがお客様にとっての1つのハードルになるのですが、有料する意味は色々あります。
他のFPオフィスとの差別化、支払ってでも相談したいという本気度など。
”有料だから勧誘一切なし”ということではなく、インパクトのあるワードでこの有料を表現していただけると嬉しいです。

色の配色やこちらにイメージに近いので選定させていただきました。

この度はご応募ありがとうございました。
どれも良く迷いました。
また今後ともよろしくお願いします

```html
<!DOCTYPE html>
<html lang="ja">
<head>
<meta charset="utf-8">
<title>2月セミナー｜くらしとおかねの窓口</title>
<link rel="stylesheet" href="https://fonts.googleapis.com/css2?family=Noto+Sans+JP:wght@400;500;700;900&display=swap">
<style>
:root{
  --blue:#1a56b0;
  --navy:#123d7d;
  --sky:#dff2fa;
  --aqua:#3ea9d6;
  --green:#3aa357;
  --green-soft:#e9f6ea;
  --orange:#f0a21c;
  --ink:#222;
  --paper:#fff;
  --code-bg:#f4f6f8;
}
*{box-sizing:border-box;margin:0;padding:0}
html,body{width:855px;height:1200px;overflow:hidden;background:var(--paper)}
body{font-family:"Noto Sans JP",sans-serif;color:var(--ink);position:relative}
.abs{position:absolute}

.hero-photo{left:430px;top:60px;width:425px;height:236px;background:linear-gradient(135deg,#e8eef3 0%,#cfdce6 55%,#b9cad8 100%)}
.headline{left:22px;top:18px;font-weight:900;color:var(--blue);font-size:54px;line-height:1.18;letter-spacing:-1px}
.brand-tag{left:560px;top:14px;font-size:13px;font-weight:700;color:var(--blue);display:flex;align-items:center;gap:5px;background:#fff;border:1px solid #cfd8e6;padding:4px 8px}
.brand-tag i{width:10px;height:10px;background:var(--green);display:block}
.month-tab{left:722px;top:12px;width:122px;height:40px;background:var(--blue);color:#fff;font-weight:700;font-size:20px;display:flex;align-items:center;justify-content:center}

.promise{left:22px;top:168px;width:440px;padding:12px 18px;background:linear-gradient(90deg,var(--blue),var(--aqua));color:#fff;font-weight:900;font-size:25px;line-height:1.35;border-radius:0 40px 40px 0}
.promise-note{left:30px;top:262px;font-size:17px;font-weight:700;color:var(--navy)}

.seminar{left:20px;width:815px;border:3px solid var(--aqua);border-radius:14px;background:#fff;padding:20px 24px 20px 140px}
.seminar.one{top:300px;height:250px}
.seminar.two{top:562px;height:238px;border-color:var(--green)}
.badge-popular{position:absolute;left:-6px;top:-14px;background:var(--orange);color:#fff;font-weight:900;font-size:16px;padding:6px 10px;border-radius:6px;transform:rotate(-8deg)}
.qr{position:absolute;left:20px;top:78px;width:104px;height:104px;background:var(--code-bg);border:3px solid var(--navy);border-radius:4px}
.two .qr{border-color:var(--green)}
.qr-label{position:absolute;left:16px;top:40px;width:112px;text-align:center;font-size:13px;font-weight:700;color:var(--navy);line-height:1.3}
.two .qr-label{color:var(--green)}
.seminar-title{font-weight:900;font-size:40px;color:var(--navy);display:flex;align-items:center;gap:10px;line-height:1.1}
.two .seminar-title{color:var(--green)}
.tag-new{font-size:15px;background:var(--navy);color:#fff;padding:3px 8px;border-radius:3px}
.subtitle{display:flex;align-items:center;gap:10px;margin-top:8px}
.level{background:var(--aqua);color:#fff;font-size:15px;font-weight:700;padding:3px 10px;border-radius:12px}
.subtitle strong{font-size:30px;font-weight:900;color:var(--blue)}
.lead{font-size:16px;font-weight:700;margin-top:6px;color:var(--ink)}
.lead.green{color:var(--green)}
.points{display:flex;gap:18px;margin-top:10px}
.points ul{list-style:none;font-size:14.5px;line-height:1.75;font-weight:500}
.points li::before{content:"✓";color:var(--aqua);font-weight:900;margin-right:6px}
.two .points li::before{color:var(--green)}
.new-mark{position:absolute;right:20px;top:14px;width:84px;height:84px;border-radius:50%;background:var(--green);color:#fff;font-weight:900;font-size:14px;display:flex;align-items:center;justify-content:center;text-align:center;line-height:1.25}
.one .new-mark{background:var(--aqua)}
.highlight{color:#d9541e;font-weight:700}

.motto{left:20px;top:812px;width:815px;height:46px;background:var(--green-soft);border-left:8px solid var(--green);color:var(--green);font-weight:900;font-size:23px;display:flex;align-items:center;padding-left:16px}
.about{left:26px;top:872px;width:520px;font-size:14.5px;line-height:1.7}
.about-photo{left:566px;top:868px;width:268px;height:130px;background:linear-gradient(135deg,#e4ecf1,#c8d8e2)}

.footer-line{left:20px;top:1008px;width:815px;height:2px;background:var(--aqua)}
.shop-name{left:26px;top:1022px;font-size:34px;font-weight:900;color:var(--navy);display:flex;align-items:center;gap:10px}
.shop-name i{width:26px;height:26px;background:var(--green);border-radius:50%;display:block}
.phone{left:26px;top:1078px;display:flex;align-items:center;gap:10px;color:var(--blue)}
.phone-num{font-size:38px;font-weight:900;letter-spacing:1px}
.hours{font-size:16px;font-weight:700;color:var(--ink)}
.notes{left:26px;top:1140px;font-size:12.5px;line-height:1.6;color:#444}
.hp-label{left:712px;top:1018px;font-size:15px;font-weight:700;color:var(--navy)}
.hp-qr{left:716px;top:1044px;width:112px;height:112px;background:var(--code-bg);border:3px solid var(--navy);border-radius:4px}
</style>
</head>
<body>

<div class="abs hero-photo" role="img" aria-label="笑顔の夫婦の写真"></div>
<h1 class="abs headline">お金を払う価値のある！<br>情報をご提供します。</h1>
<div class="abs brand-tag"><i></i>くらしとおかねの窓口</div>
<div class="abs month-tab">2月セミナー</div>

<p class="abs promise">どこのFPよりも中立に正しい<br>お金の知識が身につきます！</p>
<p class="abs promise-note">当店は特定の金融商品の勧誘を致しません。</p>

<section class="abs seminar one">
  <span class="badge-popular">人気セミナー</span>
  <p class="qr-label">こちらから<br>お申込み</p>
  <div class="qr" role="img" aria-label="iDeCo・NISAセミナー申込ページへのQRコード"></div>
  <h2 class="seminar-title">iDeCo &amp; NISA <span class="tag-new">新NISA対応</span></h2>
  <div class="subtitle"><span class="level">初心者必見</span><strong>確定拠出年金セミナー</strong></div>
  <p class="lead">あなたの疑問を金融のプロが分かりやすく解説します。</p>
  <div class="points">
    <ul>
      <li>仕組みから知りたい方に！</li>
      <li>老後準備を無理なく始めたい方</li>
      <li>投資に興味はあるが不安な方</li>
    </ul>
    <ul>
      <li>iDeCoとNISAの違いは？</li>
      <li>iDeCoとNISAどちらが良い？</li>
      <li>iDeCo・NISA向き不向き診断</li>
    </ul>
  </div>
  <div class="new-mark">最新！<br>令和6年<br>対応</div>
</section>

<section class="abs seminar two">
  <span class="badge-popular">人気セミナー</span>
  <p class="qr-label">こちらから<br>お申込み</p>
  <div class="qr" role="img" aria-label="住宅ローンセミナー申込ページへのQRコード"></div>
  <h2 class="seminar-title">住宅ローンセミナー</h2>
  <p class="lead green">住宅ローンの仕組みを専門家が分かりやすく解説します。</p>
  <p class="lead">知ると知らないで数千万円の損失も!? <span class="highlight">最新の補助金・助成金・税制優遇</span></p>
  <div class="points">
    <ul>
      <li>変動タイプ・固定タイプなど、ローンの種類がわかる</li>
      <li>購入時に注意する事、損をしない選び方</li>
      <li>返済計画の立て方と繰上げ返済のコツ</li>
    </ul>
  </div>
  <div class="new-mark">最新！<br>令和6年<br>対応</div>
</section>

<p class="abs motto">「世界に一つ、あなたの人生専用のマネープランを作ります。」</p>
<p class="abs about">マイホーム購入、将来に向けた資産形成、そんなお悩みを中立な立場で整理します。私たちは「中立」のファイナンシャルプランナーが、お客様の家計を丁寧に分析し、無理のない計画をご提案します。住まいとお金のことをワンストップで解決。一人ひとりに寄り添い、10年後・20年後も安心できる暮らしをお手伝いいたします。</p>
<div class="abs about-photo" role="img" aria-label="相談窓口で話す担当者と来店客の写真"></div>

<div class="abs footer-line"></div>
<div class="abs shop-name"><i></i>くらしとおかねの窓口</div>
<div class="abs phone">
  <svg width="34" height="34" viewBox="0 0 24 24" aria-hidden="true"><path fill="#1a56b0" d="M6.6 10.8a15.1 15.1 0 0 0 6.6 6.6l2.2-2.2a1 1 0 0 1 1-.25 11.4 11.4 0 0 0 3.6.57 1 1 0 0 1 1 1V20a1 1 0 0 1-1 1A17 17 0 0 1 3 4a1 1 0 0 1 1-1h3.5a1 1 0 0 1 1 1c0 1.25.2 2.45.57 3.57a1 1 0 0 1-.25 1z"/></svg>
  <span class="phone-num">097-555-0184</span>
  <span class="hours">受付時間：10:00～17:00</span>
</div>
<p class="abs notes">※申込みの際は、お名前・ご住所・電話番号・希望日時をお伝えください。<br>主催：株式会社ミナトプランニング（共催／運営サポート：株式会社ユイ）</p>
<p class="abs hp-label">店舗HPはこちら</p>
<div class="abs hp-qr" role="img" aria-label="店舗ホームページへのQRコード"></div>

</body>
</html>
```